731 Orchard Avenue Residences

designing a sign for apartment complex;
prefer colors gray white and yellow

Target Market(s)

residents coming home to their apartment

Font styles to use
Serif
Sans Serif

Colors
FFF300
FFF600
FEFA6F
FFFEC7
FFFEE8

Requirements
Must have
• black or gray, white and some yellow; easy to read and see

```html
<!DOCTYPE html>
<html lang="en">
<head>
<meta charset="utf-8">
<title>731 Orchard Avenue Residences – Entrance Sign</title>
<link rel="stylesheet" href="https://fonts.googleapis.com/css2?family=Cinzel:wght@700&display=swap">
<style>
  :root {
    --page-bg: #fdfdfd;
    --sign-frame: #747474;
    --sign-trim: #fff300;
    --sign-face: #2b2a28;
    --sign-text: #ffffff;
    --emblem-fill: #fff600;
    --divider-fill: rgba(255, 255, 255, 0.22);
    --sign-shadow: rgba(0, 0, 0, 0.45);
  }
  html, body {
    margin: 0;
    padding: 0;
    width: 1200px;
    height: 1200px;
    overflow: hidden;
    background: var(--page-bg);
  }
  .canvas {
    width: 1200px;
    height: 1200px;
    display: block;
  }
  .sign-frame {
    fill: var(--sign-frame);
    filter: drop-shadow(0 14px 10px var(--sign-shadow));
  }
  .sign-trim { fill: var(--sign-trim); }
  .sign-face { fill: var(--sign-face); }
  .sign-emblem { fill: var(--emblem-fill); }
  .sign-divider { fill: var(--divider-fill); }
  .sign-number,
  .sign-name {
    font-family: "Cinzel", "Times New Roman", serif;
    font-weight: 700;
    fill: var(--sign-text);
    text-anchor: middle;
  }
  .sign-number { font-size: 88px; letter-spacing: 2px; }
  .sign-name { font-size: 82px; letter-spacing: 1px; }
</style>
</head>
<body>
<svg class="canvas" viewBox="0 0 1200 1200" xmlns="http://www.w3.org/2000/svg" role="img" aria-label="731 Orchard Avenue Residences entrance sign">
  <path class="sign-frame" d="M114,412 C300,422 440,280 600,280 C760,280 900,422 1086,412 L1086,922 L114,922 Z"/>
  <path class="sign-trim" d="M136,438 C310,440 450,301 600,301 C750,301 890,440 1064,438 L1064,902 L136,902 Z"/>
  <path class="sign-face" d="M154,458 C320,456 460,319 600,319 C740,319 880,456 1046,458 L1046,884 L154,884 Z"/>

  <rect class="sign-emblem" x="564" y="346" width="72" height="96" rx="30" role="img" aria-label="Yellow heraldic lily emblem"/>

  <text class="sign-number" x="600" y="516">731</text>
  <text class="sign-name" x="600" y="602">Orchard</text>
  <text class="sign-name" x="600" y="690">Avenue</text>
  <text class="sign-name" x="600" y="776">Residences</text>

  <rect class="sign-divider" x="334" y="822" width="532" height="24" rx="12" role="img" aria-label="White scrolled flourish divider"/>
</svg>
</body>
</html>
```